Wordpress Design ProjectWP website design (Vosberg)

We need a wordpress design that will incorporate a professional color scheme with company logo in a clean layout. The design needs to consider that this will be developed on a responsive theme. Colors are undetermined - use a colors in logo - maybe a light color, maybe yellow accent, and black. Client wants a 'modern' look.

Industry/Entity Type

It Company

Font styles to use
Serif
Sans Serif

Requirements
Must have
• Navigation: 1) Home 2) Auctions 3) Services 4) About Us 5) Contact us
• Site will have a slideshow element (initial image attached) and the following widgets: 1)Social Media (facebook,RSS) 2) Email Sign Up Form 3) Featured Video, 4) Auction Search
• Homepage content: "Vosberg Auction & Real Estate
• Since 1958 We at Vosberg Auction & Real Estate have offered our services to our clients as a versatile Auction Company with the ability to perform a variety of Auction types.
• Having sold Items such as: Real Estate, Machinery, Antiques, Tools, and much, more; we have constructed a strong foundation of knowledge and experience of the appropriate Auction marketing and preparation logistics. This results in a high quality Auction service that we provide to our clients, and also a level of service that we take great pride in.
• When you are ready for your Auction, you want it done right!
• Call Us at Vosberg Auction & Real Estate,"
• In the footer, there will be smaller company logo, the affiliations logo (attached), and contact info below:
• Vosberg Auction, Inc.
• 4135 County Highway 82
• Dunmore Hollow, VT 05921
• 607-555-0143
Nice to have
• Use of a dropdown menu with styling.

```html
<!DOCTYPE html>
<html lang="en">
<head>
<meta charset="utf-8">
<title>Vosberg Auction &amp; Real Estate</title>
<link href="https://fonts.googleapis.com/css2?family=PT+Sans:wght@400;700&family=PT+Sans+Narrow&family=Arimo&display=swap" rel="stylesheet">
<style>
:root{
  --navy:#14143a;
  --black:#000;
  --white:#fff;
  --text:#333;
  --muted:#888;
  --line:#c9c9c9;
  --field:#f4f4f4;
  --accent:#e3001b;
  --footer-text:#ddd;
}
*{box-sizing:border-box;margin:0;padding:0}
html,body{width:1044px;height:1200px;overflow:hidden;background:var(--white)}
body{position:relative;font-family:"PT Sans",sans-serif;color:var(--text)}
.abs{position:absolute}

/* header */
.brand{left:96px;top:30px;display:flex;align-items:center;gap:8px;font-size:38px;font-weight:700;color:var(--navy);letter-spacing:1px}
.brand-mark{width:14px;height:14px;background:var(--navy)}
.call-badge{left:750px;top:36px;width:78px;height:21px;background:var(--navy);border-radius:3px;color:var(--white);font-size:12px;display:flex;align-items:center;justify-content:center;gap:5px}
.header-phone{left:844px;top:30px;font-family:"PT Sans Narrow",sans-serif;font-size:27px;color:var(--navy);line-height:32px}
.search{left:613px;top:67px;width:344px;height:27px;border:1px solid #d8d8d8;border-radius:3px;background:var(--field);font-size:11px;color:var(--muted);padding:7px 9px}
.search svg{position:absolute;right:8px;top:7px}

/* navigation */
.nav{left:0;top:109px;width:1044px;height:33px;background:var(--navy)}
.nav ul{list-style:none;position:absolute;left:91px;top:0;display:flex;height:33px;align-items:center}
.nav li{color:var(--white);font-size:13.5px;padding:0 13px;border-left:1px solid #3a3a5c;line-height:20px}
.nav li:first-child{border-left:0}
.social{right:94px;top:117px;display:flex;gap:4px}
.social span{width:18px;height:18px;border-radius:50%;background:var(--white)}

/* slider */
.slider{left:87px;top:151px;width:628px;height:248px;background:linear-gradient(135deg,#6e7f52,#3d5a2a 45%,#7b6a5a);}
.slider-caption{left:0;bottom:0;width:628px;height:53px;background:rgba(0,0,0,.72);color:var(--white);padding:7px 14px}
.slider-caption h2{font-weight:400;font-size:21px;line-height:25px}
.slider-caption p{font-size:11.5px}
.dots{right:9px;bottom:9px;display:flex;gap:4px}
.dots i{width:10px;height:10px;border-radius:50%;background:var(--white)}
.dots i.on{background:var(--accent)}
.side-photo{left:726px;width:231px;height:120px}

/* section headings */
.section-head{border-top:2px solid var(--black);border-bottom:1px solid var(--black);height:28px;font-size:13.5px;color:var(--navy);padding:5px 4px}

/* intro */
.intro{left:92px;top:462px;width:612px}
.intro h3{font-size:13.5px;font-weight:400;color:var(--black);margin-bottom:4px}
.intro p{font-size:11.3px;line-height:17.4px;text-align:justify;margin-bottom:7px}

/* listings */
.listing-title{left:87px;width:628px;border-bottom:1px solid var(--line);font-size:13.5px;color:var(--black);padding:0 5px 3px}
.listing-photo{left:87px;width:231px;height:124px}
.listing-text{left:333px;width:370px;font-size:11.3px;line-height:17.4px;text-align:justify}
.stars{left:333px;font-size:17px;color:var(--black);letter-spacing:1px}
.btn{height:21px;background:var(--black);color:var(--white);font-size:10.5px;display:flex;align-items:center;justify-content:center;gap:6px}
.pager{top:967px;height:19px;border:1px solid var(--black);font-size:11px;display:flex;align-items:center;justify-content:center;color:var(--black)}
.pager.disabled{border-color:#e2e2e2;color:#ccc}
.pager.current{background:var(--black);color:var(--white)}

/* sidebar */
.search-box{left:726px;top:450px;width:231px;height:176px;border:1px solid #e4e4e4}
.field{border:1px solid #ccc;border-radius:2px;font-family:Arimo,sans-serif;font-size:10.5px;color:var(--muted);padding:6px 7px;background:var(--white)}
.field.select{background:linear-gradient(#fff,#eee)}
.range-label{left:733px;top:531px;font-family:Arimo,sans-serif;font-size:11.5px;color:#555}
.range-track{left:733px;top:554px;width:218px;height:5px;border:1px solid #bbb;border-radius:3px;background:#eee}
.range-fill{left:772px;top:555px;width:88px;height:3px;background:#9aa7bd}
.range-knob{top:550px;width:9px;height:12px;border:1px solid #999;border-radius:2px;background:#f7f7f7}
.range-val{top:567px;font-family:Arimo,sans-serif;font-size:10.5px;color:#555}
.submit{left:734px;top:594px;width:99px;height:25px;background:var(--black);color:var(--white);font-family:Arimo,sans-serif;font-size:13px;display:flex;align-items:center;justify-content:center}
.video{left:726px;top:637px;width:231px;height:156px;background:linear-gradient(160deg,#a99c7a,#6f6248 55%,#4e5a36)}
.play{left:814px;top:697px;width:54px;height:38px;border-radius:7px;background:rgba(0,0,0,.7);border:2px solid rgba(255,255,255,.5)}
.signup{left:726px;top:831px;width:231px;height:126px;background:var(--black)}
.signup-field{left:737px;width:210px;height:28px;border:1px solid #444;border-radius:3px;background:#0a0a0a;color:#eee;font-family:Arimo,sans-serif;font-size:12px;display:flex;align-items:center;gap:8px;padding-left:9px}
.subscribe{left:737px;top:923px;width:99px;height:24px;background:linear-gradient(#fff,#ddd);border-radius:2px;color:var(--black);font-family:Arimo,sans-serif;font-size:13px;display:flex;align-items:center;justify-content:center}

/* footer */
.footer{left:0;top:994px;width:1044px;height:175px;background:var(--black)}
.badge-round{left:100px;top:1052px;width:120px;height:86px;border-radius:50%;border:3px solid var(--white)}
.badge-square{left:244px;top:1056px;width:61px;height:70px;background:var(--white)}
.footer-brand{right:88px;top:1016px;display:flex;align-items:center;gap:5px;background:var(--white);color:var(--navy);font-size:14px;font-weight:700;padding:8px 7px}
.footer-brand i{width:7px;height:7px;background:var(--navy)}
.footer-contact{right:88px;top:1061px;text-align:right;color:var(--white)}
.footer-contact h4{font-size:14px;font-weight:700;line-height:20px;color:var(--white)}
.footer-contact p{font-size:12px;line-height:17.5px;color:var(--footer-text)}
.footer-pin{left:806px;top:1085px}
.footer-phone{right:88px;top:1130px;font-size:15px;display:flex;align-items:center;gap:10px;color:var(--white)}
.copyright{left:0;top:1169px;width:1044px;height:31px;background:var(--navy);color:var(--footer-text);font-size:10px;display:flex;align-items:center;justify-content:center}
.copyright b{color:var(--white);font-weight:700;margin-left:3px}
</style>
</head>
<body>

<header>
  <div class="abs brand"><span>VOSBERG</span><i class="brand-mark"></i></div>
  <div class="abs call-badge">
    <svg width="11" height="11" viewBox="0 0 24 24"><path fill="#fff" d="M6.6 10.8a15 15 0 0 0 6.6 6.6l2.2-2.2c.3-.3.7-.4 1-.2 1.1.4 2.3.6 3.6.6.6 0 1 .4 1 1V20c0 .6-.4 1-1 1A17 17 0 0 1 3 4c0-.6.4-1 1-1h3.5c.6 0 1 .4 1 1 0 1.3.2 2.5.6 3.6.1.3 0 .7-.2 1z"/></svg>
    CALL US
  </div>
  <div class="abs header-phone">607-555-0143</div>
  <div class="abs search">Search
    <svg width="12" height="12" viewBox="0 0 24 24"><circle cx="10" cy="10" r="6.5" fill="none" stroke="#111" stroke-width="3"/><path d="M15 15l6 6" stroke="#111" stroke-width="3.5" stroke-linecap="round"/></svg>
  </div>
</header>

<nav class="abs nav">
  <ul>
    <li>HOME</li><li>AUCTIONS</li><li>SERVICES</li><li>ABOUT US</li><li>CONTACT US</li>
  </ul>
</nav>
<div class="abs social"><span></span><span></span><span></span><span></span></div>

<section class="abs slider" role="img" aria-label="Auctioneer pointing over a large crowd gathered around green tractors">
  <div class="abs slider-caption">
    <h2>Vosberg Auction &amp; Real Estate</h2>
    <p>Since 1958 We at Vosberg Auction &amp; Real Estate have offered our services to our clients......</p>
  </div>
  <div class="abs dots"><i class="on"></i><i></i><i></i><i></i><i></i></div>
</section>
<div class="abs side-photo" style="top:151px;background:linear-gradient(#7fa8d8,#b9cfe6 45%,#3f7a32 60%,#2f6326)" role="img" aria-label="Green harvesting machine in a crop field"></div>
<div class="abs side-photo" style="top:279px;background:linear-gradient(160deg,#c89452,#a8672e 60%,#b97d40)" role="img" aria-label="Combine harvester working a golden wheat field"></div>

<main>
  <div class="abs section-head" style="left:87px;top:422px;width:628px">LATEST AUCTION REVIEW</div>
  <article class="abs intro">
    <h3>Vosberg Auction &amp; Real Estate</h3>
    <p>Since 1958 We at Vosberg Auction &amp; Real Estate have offered our services to our clients as a versatile Auction Company with the ability to perform a variety of Auction types.</p>
    <p>Having sold Items such as: Real Estate, Machinery, Antiques, Tools, and much, more; we have constructed a strong foundation of knowledge and experience of the appropriate Auction marketing and preparation logistics. This results in a high quality Auction service that we provide to our clients, and also a level of service that we take great pride in.</p>
  </article>

  <div class="abs listing-title" style="top:614px">Lorem ipsum dolor sit amet, consectetuer</div>
  <div class="abs listing-photo" style="top:646px;background:linear-gradient(150deg,#4f6a3a,#7d8a6a 50%,#9a8a70)" role="img" aria-label="Forestry forwarder machine beside stacked logs"></div>
  <p class="abs listing-text" style="top:646px">Fusce euismod consequat ante. Lorem ipsum dolor sit amet, consectetuer adipiscing elit. Pellentesque sed dolor. Aliquam congue fermentum nisl. Mauris accumsan nulla vel diam. Sed in lacus ut enim adipiscing aliquet. Nulla venenatis. In pede mi, aliquet sit amet</p>
  <div class="abs stars" style="top:724px">★★★★</div>
  <div class="abs btn" style="left:333px;top:749px;width:93px">
    <svg width="10" height="10" viewBox="0 0 24 24"><circle cx="10" cy="10" r="6.5" fill="none" stroke="#fff" stroke-width="3"/><path d="M15 15l6 6" stroke="#fff" stroke-width="3.5"/></svg>QUICK VIEW</div>
  <div class="abs btn" style="left:430px;top:749px;width:61px">DETAILS</div>

  <div class="abs listing-title" style="top:801px">Lorem ipsum dolor sit amet, consectetuer</div>
  <div class="abs listing-photo" style="top:833px;background:linear-gradient(#bcd0e6,#dfe6ee 40%,#c9a84f 62%,#8a9a4a)" role="img" aria-label="Green telehandler lifting hay bales in a field"></div>
  <p class="abs listing-text" style="top:833px">Fusce euismod consequat ante. Lorem ipsum dolor sit amet, consectetuer adipiscing elit. Pellentesque sed dolor. Aliquam congue fermentum nisl. Mauris accumsan nulla vel diam. Sed in lacus ut enim adipiscing aliquet. Nulla venenatis. In pede mi, aliquet sit amet</p>
  <div class="abs stars" style="top:911px">★★★★★</div>
  <div class="abs btn" style="left:333px;top:936px;width:93px">
    <svg width="10" height="10" viewBox="0 0 24 24"><circle cx="10" cy="10" r="6.5" fill="none" stroke="#fff" stroke-width="3"/><path d="M15 15l6 6" stroke="#fff" stroke-width="3.5"/></svg>QUICK VIEW</div>
  <div class="abs btn" style="left:430px;top:936px;width:61px">DETAILS</div>

  <div class="abs pager disabled" style="left:578px;width:50px">previous</div>
  <div class="abs pager current" style="left:632px;width:16px">1</div>
  <div class="abs pager" style="left:652px;width:17px">2</div>
  <div class="abs pager" style="left:673px;width:32px">next</div>
</main>

<aside>
  <div class="abs section-head" style="left:726px;top:422px;width:231px">AUCTION SEARCH</div>
  <div class="abs search-box"></div>
  <div class="abs field" style="left:733px;top:457px;width:218px;height:25px">Filter by keywords</div>
  <div class="abs field select" style="left:733px;top:492px;width:105px;height:25px">Type of house</div>
  <div class="abs field select" style="left:846px;top:492px;width:105px;height:25px">City</div>
  <div class="abs range-label">Pricerange</div>
  <div class="abs range-track"></div>
  <div class="abs range-fill"></div>
  <div class="abs range-knob" style="left:768px"></div>
  <div class="abs range-knob" style="left:855px"></div>
  <div class="abs range-val" style="left:750px">$110,000</div>
  <div class="abs range-val" style="left:836px">$450,000</div>
  <div class="abs submit">Submit</div>

  <div class="abs video" role="img" aria-label="Featured video still of a couple viewing a house"></div>
  <div class="abs play"><svg width="50" height="34" viewBox="0 0 50 34"><path d="M20 9l13 8-13 8z" fill="#fff"/></svg></div>

  <div class="abs section-head" style="left:726px;top:804px;width:231px">EMAIL SIGN UP FORM</div>
  <div class="abs signup"></div>
  <div class="abs signup-field" style="top:842px">
    <svg width="13" height="10" viewBox="0 0 13 10"><rect x=".5" y=".5" width="12" height="9" fill="none" stroke="#888"/><path d="M.5.5l6 5 6-5" fill="none" stroke="#888"/></svg>Enter your email</div>
  <div class="abs signup-field" style="top:879px">
    <svg width="12" height="12" viewBox="0 0 12 12"><circle cx="6" cy="3.5" r="3" fill="#888"/><path d="M0 12c0-4 3-5 6-5s6 1 6 5z" fill="#888"/></svg>Enter your name</div>
  <div class="abs subscribe">Subscribe</div>
</aside>

<footer>
  <div class="abs footer"></div>
  <div class="abs badge-round" role="img" aria-label="State auctioneers association membership badge"></div>
  <div class="abs badge-square" role="img" aria-label="National auctioneers association membership badge"></div>
  <div class="abs footer-brand"><span>VOSBERG</span><i></i></div>
  <div class="abs footer-contact">
    <h4>VOSBERG AUCTION, INC.</h4>
    <p>4135 County Highway 82</p>
    <p>Dunmore Hollow, VT 05921</p>
  </div>
  <svg class="abs footer-pin" width="12" height="17" viewBox="0 0 12 17"><path d="M6 0a6 6 0 0 0-6 6c0 4.5 6 11 6 11s6-6.5 6-11a6 6 0 0 0-6-6z" fill="#bbb"/><circle cx="6" cy="6" r="2.2" fill="#000"/></svg>
  <div class="abs footer-phone">
    <svg width="13" height="13" viewBox="0 0 24 24"><path fill="#ddd" d="M6.6 10.8a15 15 0 0 0 6.6 6.6l2.2-2.2c.3-.3.7-.4 1-.2 1.1.4 2.3.6 3.6.6.6 0 1 .4 1 1V20c0 .6-.4 1-1 1A17 17 0 0 1 3 4c0-.6.4-1 1-1h3.5c.6 0 1 .4 1 1 0 1.3.2 2.5.6 3.6.1.3 0 .7-.2 1z"/></svg>
    607-555-0143</div>
  <div class="abs copyright">© Copyright 2014, all rights reserved with <b>Vosberg Auction, Inc.</b></div>
</footer>

</body>
</html>
```